Site Design - PSD Only - festival management

We are looking for a final design for our B2B marketplace. The project is a social commerce platform managing the application and transaction process for festivals and local events. The site design should be based on either Bootstrap or Zurb Foundation. We will provide logos and example images.

Two of the most critical pages will be the home page and the search interface, as well several dashboards. Beyond that, most of the pages will be standard forms and other typical pages that drop into the general site theme. The design tends towards minimalism to simplify the UX and speed up the interface. It incorporates elements from the the following websites. Although the wireframes may lift design elements directly from some of these sites, we are looking for a design that incorporates them more as inspiration.

quilo.co - good example of minimalist structure on internal pages
ravtorn.com - some similarities on search pages, etc.
vexdal.com - nice simple layout for features on home and internal pages
mossbrackle.com - nice alternative to standard bootstrap template

We're nearing the end of this project.  I've received some good submissions , but they are all variations on the exact same theme.  I would still like to see something that doesn't look like a bootstrap template.  I suggested the following idea to a few of the submitters, but now I am adding it to the main project description in hopes of stoking the engine.

The idea I had is for something a little less "bootstrappy" riffs on the design at mossbrackle.com with a flat background color that nicely offsets the blue in the logo. Rather than pulling in a stock image I thought about creating a derivation of the iconic Harrowmere poster, perhaps with vendor tents as tuning pegs and a silhouette of people on the neck. Just throwing that out there. 

I'm not a designer, though, so here's hoping we can see some different ideas while the project is still open.

Thanks.

Target Market(s)

Target market: Festival and event organizers; event participants including exhibitors, vendors, musicians, authors, volunteers, etc.

Industry/Entity Type

Festival

Requirements
Must have
• Home page, Search page, User dash, Organization dash, Event dash, Features, FAQ, various forms
Nice to have
• Would like to see some alternative designs to the standard bootstrap templates...creativity is encouraged.
Should not have
• Should not look like it was pulled off of the shelf.

```html
<!DOCTYPE html>
<html lang="en">
<head>
<meta charset="utf-8">
<title>Festlyn — Festival Management</title>
<link href="https://fonts.googleapis.com/css2?family=Dosis:wght@400;500;600;800&family=Open+Sans:wght@400;600&display=swap" rel="stylesheet">
<style>
  :root{
    --blue:#1f7ec4;
    --blue-dark:#17659f;
    --ink:#333b42;
    --muted:#7a8288;
    --line:#dfe2e5;
    --page:#ffffff;
    --footer:#3b3d40;
    --footer-deep:#2e3033;
    --footer-text:#c8ccd0;
    --icon-bg:#e9ecef;
  }
  *{box-sizing:border-box;margin:0;padding:0}
  html,body{width:841px;height:1200px;overflow:hidden;background:var(--page)}
  body{font-family:"Open Sans",sans-serif;color:var(--ink)}
  .site{position:relative;width:841px;height:1200px;overflow:hidden}

  /* header */
  .brand{position:absolute;left:34px;top:18px;display:flex;align-items:center;gap:8px}
  .brand-dot{width:26px;height:26px;border-radius:50%;background:var(--blue)}
  .brand-name{font-family:"Dosis",sans-serif;font-weight:800;font-size:28px;letter-spacing:1px;color:var(--ink)}
  .stats{position:absolute;top:14px;right:30px;display:flex}
  .stat{width:125px;text-align:center;padding:0 8px;border-left:1px solid var(--line)}
  .stat:first-child{border-left:none}
  .stat-title{font-family:"Dosis",sans-serif;font-weight:600;font-size:14px;color:var(--blue);letter-spacing:.5px}
  .stat-text{font-size:8px;color:var(--muted);line-height:1.3}
  .nav{position:absolute;top:68px;left:262px;display:flex;gap:14px;font-size:10.5px;color:var(--ink)}
  .socials{position:absolute;top:65px;right:34px;display:flex;gap:6px}
  .social{width:18px;height:18px;border-radius:50%;background:var(--blue)}

  /* hero */
  .hero{position:absolute;left:0;top:95px;width:841px;height:330px;
    background:linear-gradient(160deg,#b9c4cc 0%,#8a9199 30%,#5e6a55 60%,#7c6f5e 100%)}
  .hero-shade{position:absolute;inset:0;background:linear-gradient(180deg,rgba(0,0,0,0) 40%,rgba(0,0,0,.25) 100%)}
  .hero-title{position:absolute;left:0;right:0;top:152px;text-align:center;font-family:"Dosis",sans-serif;font-weight:800;font-size:62px;letter-spacing:4px;color:#fff}
  .hero-sub{position:absolute;left:240px;top:232px;width:400px;font-family:"Dosis",sans-serif;font-weight:600;font-size:16px;line-height:1.35;color:#fff}
  .btn-hero{position:absolute;left:618px;top:268px;width:130px;height:38px;background:var(--blue);color:#fff;font-family:"Dosis",sans-serif;font-weight:600;font-size:16px;display:flex;align-items:center;justify-content:center}

  /* features */
  .features{position:absolute;left:98px;top:448px;width:646px;display:grid;grid-template-columns:repeat(3,1fr);column-gap:18px;row-gap:16px}
  .feature{height:192px;padding:14px 14px 0;text-align:center;border-bottom:1px solid var(--line)}
  .feature.is-active{border:1px solid var(--line)}
  .feature-icon{width:40px;height:40px;margin:0 auto 8px;border-radius:50%;background:var(--icon-bg);display:flex;align-items:center;justify-content:center}
  .feature-title{font-family:"Dosis",sans-serif;font-weight:500;font-size:16.5px;color:var(--ink);line-height:1.1;margin-bottom:7px}
  .feature-text{font-size:7.5px;line-height:1.45;color:var(--muted);text-align:left}
  .btn-small{display:inline-block;margin-top:8px;padding:4px 10px;background:var(--blue);color:#fff;font-size:7.5px}

  /* why */
  .why-photo{position:absolute;left:98px;top:882px;width:322px;height:196px;
    background:radial-gradient(ellipse at 55% 35%,#6c7fb8 0%,#3c3f74 45%,#1f1d33 100%)}
  .why{position:absolute;left:444px;top:884px;width:300px}
  .why-title{font-family:"Dosis",sans-serif;font-weight:500;font-size:19px;color:var(--ink);margin-bottom:10px}
  .why-text{font-size:8px;line-height:1.5;color:var(--muted);margin-bottom:9px}

  /* footer */
  .footer{position:absolute;left:0;top:1098px;width:841px;height:102px;background:var(--footer);color:var(--footer-text)}
  .newsletter{position:absolute;left:98px;top:14px}
  .footer-label{font-size:10px;color:#fff;margin-bottom:6px}
  .signup{display:flex}
  .signup-input{width:160px;height:24px;background:#55585c;font-size:8px;color:#9ca1a6;padding:6px 8px}
  .signup-btn{width:62px;height:24px;background:var(--blue);color:#fff;font-size:9px;font-weight:600;display:flex;align-items:center;justify-content:center}
  .contact{position:absolute;left:416px;top:20px;font-size:9.5px;line-height:1.7;color:#fff}
  .follow{position:absolute;right:96px;top:16px;text-align:center}
  .follow .socials{position:static;margin-top:6px}
  .legal{position:absolute;left:0;bottom:0;width:100%;height:30px;background:var(--footer-deep);font-size:8px;display:flex;align-items:center;justify-content:space-between;padding:0 96px}
</style>
</head>
<body>
<div class="site">

  <header>
    <div class="brand"><span class="brand-dot"></span><span class="brand-name">FESTLYN</span></div>
    <div class="stats">
      <div class="stat"><div class="stat-title">APPLY</div><div class="stat-text">to festivals in local areas</div></div>
      <div class="stat"><div class="stat-title">ADD</div><div class="stat-text">your event to the network</div></div>
      <div class="stat"><div class="stat-title">JOIN</div><div class="stat-text">thousands of festival professionals</div></div>
    </div>
    <nav class="nav"><span>About</span><span>Features</span><span>Pay</span><span>Blog</span><span>Press</span><span>Register</span><span>Login</span></nav>
    <div class="socials"><span class="social"></span><span class="social"></span><span class="social"></span></div>
  </header>

  <section class="hero" role="img" aria-label="Photo of a crowd of festival visitors outdoors in autumn">
    <div class="hero-shade"></div>
    <h1 class="hero-title">PEACE OF MIND</h1>
    <p class="hero-sub">Welcome to Festlyn, we connect festival and event organizers with the people that make it happen.</p>
    <a class="btn-hero">Get Started</a>
  </section>

  <section class="features">
    <div class="feature is-active">
      <div class="feature-icon"><svg width="20" height="20" viewBox="0 0 20 20"><rect x="3" y="6" width="14" height="11" fill="none" stroke="#333b42" stroke-width="1.6"/><path d="M3 6l7 5 7-5" fill="none" stroke="#333b42" stroke-width="1.6"/></svg></div>
      <h3 class="feature-title">Online Applications</h3>
      <p class="feature-text">Lorem ipsum dolor sit amet, consectetur adipiscing elit. Quisque suscipit laoreet justo, a facilisis diam tortor a. Aliquam ac consectetur tellus. Aenean orci.</p>
      <a class="btn-small">Learn More</a>
    </div>
    <div class="feature">
      <div class="feature-icon"><svg width="20" height="20" viewBox="0 0 20 20"><rect x="3" y="4" width="14" height="13" fill="none" stroke="#333b42" stroke-width="1.6"/><path d="M3 8h14M7 2v4M13 2v4" stroke="#333b42" stroke-width="1.6"/></svg></div>
      <h3 class="feature-title">Integrated Scheduling</h3>
      <p class="feature-text">Lorem ipsum dolor sit amet, consectetur adipiscing elit. Quisque suscipit laoreet justo, a facilisis diam tortor a. Aliquam ac consectetur tellus. Aenean nunc neque, consequat id enim leo.</p>
      <a class="btn-small">Learn More</a>
    </div>
    <div class="feature">
      <div class="feature-icon"><svg width="20" height="20" viewBox="0 0 20 20"><rect x="6" y="2" width="8" height="16" rx="1.5" fill="none" stroke="#333b42" stroke-width="1.6"/><circle cx="10" cy="15.5" r="1" fill="#333b42"/></svg></div>
      <h3 class="feature-title">Native iOS &amp; Android Apps</h3>
      <p class="feature-text">Lorem ipsum dolor sit amet, consectetur adipiscing elit. Quisque suscipit laoreet justo, a facilisis diam tortor a. Aliquam ac consectetur tellus. Aenean nunc neque, consequat id enim leo.</p>
      <a class="btn-small">Learn More</a>
    </div>
    <div class="feature">
      <div class="feature-icon"><svg width="20" height="20" viewBox="0 0 20 20"><path d="M4 17V11M8 17V7M12 17V9M16 17V4" stroke="#333b42" stroke-width="2"/></svg></div>
      <h3 class="feature-title">Real-time Analytics</h3>
      <p class="feature-text">Lorem ipsum dolor sit amet, consectetur adipiscing elit. Quisque suscipit laoreet justo, a facilisis diam tortor a. Aliquam ac consectetur tellus. Aenean nunc neque, consequat id enim leo.</p>
      <a class="btn-small">Learn More</a>
    </div>
    <div class="feature">
      <div class="feature-icon"><svg width="20" height="20" viewBox="0 0 20 20"><circle cx="5" cy="10" r="2.2" fill="#333b42"/><circle cx="15" cy="5" r="2.2" fill="#333b42"/><circle cx="15" cy="15" r="2.2" fill="#333b42"/><path d="M5 10L15 5M5 10l10 5" stroke="#333b42" stroke-width="1.4"/></svg></div>
      <h3 class="feature-title">Social Network Integration</h3>
      <p class="feature-text">Lorem ipsum dolor sit amet, consectetur adipiscing elit. Quisque suscipit laoreet justo, a facilisis diam tortor a. Aliquam ac consectetur tellus. Aenean nunc neque, consequat id enim leo.</p>
      <a class="btn-small">Learn More</a>
    </div>
    <div class="feature">
      <div class="feature-icon"><svg width="20" height="20" viewBox="0 0 20 20"><rect x="2" y="5" width="16" height="10" fill="none" stroke="#333b42" stroke-width="1.6"/><circle cx="10" cy="10" r="2.4" fill="none" stroke="#333b42" stroke-width="1.4"/></svg></div>
      <h3 class="feature-title">Enhanced Sponsorship Opportunities</h3>
      <p class="feature-text">Lorem ipsum dolor sit amet, consectetur adipiscing elit. Quisque suscipit laoreet justo, a facilisis diam tortor a. Aliquam ac consectetur tellus.</p>
      <a class="btn-small">Learn More</a>
    </div>
  </section>

  <div class="why-photo" role="img" aria-label="Photo of a concert hall lit in blue and purple during an event"></div>
  <section class="why">
    <h2 class="why-title">Why you should book with us</h2>
    <p class="why-text">Lorem ipsum dolor sit amet, consectetur adipiscing elit. Quisque suscipit laoreet justo, a facilisis diam tortor a. Aliquam ac consectetur tellus. Aenean nunc neque, consequat id enim leo.</p>
    <p class="why-text">Lorem ipsum dolor sit amet, consectetur adipiscing elit. Quisque suscipit laoreet justo, a facilisis diam tortor a. Aliquam ac consectetur tellus.</p>
    <p class="why-text">Lorem ipsum dolor sit amet, consectetur adipiscing elit. Quisque suscipit laoreet justo, a facilisis diam tortor a. Aliquam ac consectetur tellus. Aenean nunc neque, consequat id enim leo.</p>
  </section>

  <footer class="footer">
    <div class="newsletter">
      <div class="footer-label">Newsletter Signup</div>
      <div class="signup"><span class="signup-input">enter email address</span><span class="signup-btn">SUBMIT</span></div>
    </div>
    <div class="contact">hello@festlyn.com<br>(800) 555-0148</div>
    <div class="follow">
      <div class="footer-label">Follow us on</div>
      <div class="socials"><span class="social"></span><span class="social"></span><span class="social"></span></div>
    </div>
    <div class="legal"><span>Privacy Policy &nbsp;|&nbsp; Terms &amp; Conditions</span><span>© 2015 Festlyn. All Rights Reserved.</span></div>
  </footer>

</div>
</body>
</html>
```